Flyer for Belcrest Family Dental

we need a flyer to advertise our office and to bring new patients, usually flyers include a group of family smiling, but I have seen cartoons also,
The name of the clinic is Belcrest Family dental, address 4382 W Dunlow rd, Katy, TX 77583 , no phone number yet, but you can use any 10 digit number , I don’t have or own any images yet , please the source files of the winner need to have images and the text fields on separate layers to edit if needed promotions, business hours, etc

Target Market(s)

Patient in need of dental work

Industry/Entity Type

Dental Clinic

Font styles to use
Serif
Sans Serif
Script

Colors
34a6d7
0792cd
abd037
9bcb3c
33b8a4

Requirements
Must have
• Images of a family showing their smile
Nice to have
• Design including blue and green colors,
• front and back,
• a section for map location,

```html
<!DOCTYPE html>
<html lang="en">
<head>
<meta charset="utf-8">
<title>Belcrest Family Dental – Flyer Front and Back</title>
<link href="https://fonts.googleapis.com/css2?family=Permanent+Marker&family=Source+Sans+3:wght@400;600;700&family=Ubuntu:wght@400;500;700&display=swap" rel="stylesheet">
<style>
  :root{
    --stage:#383a39;
    --blue:#0792cd;
    --blue-light:#34a6d7;
    --green:#abd037;
    --green-deep:#9bcb3c;
    --navy:#1f2d3a;
    --ink:#222;
    --white:#fff;
  }
  *{margin:0;padding:0;box-sizing:border-box}
  html,body{width:1200px;height:1200px;overflow:hidden;background:var(--stage)}
  .stage{position:relative;width:1200px;height:1200px;font-family:"Source Sans 3",sans-serif}
  .page{position:absolute;overflow:hidden;background:var(--blue)}
  .page--front{left:64px;top:229px;width:528px;height:739px}
  .page--back{left:619px;top:231px;width:526px;height:737px}
  .page svg.art{position:absolute;inset:0}
  .abs{position:absolute}
  .headline{font-family:"Permanent Marker","Arial Narrow",cursive;color:var(--white);line-height:1;white-space:nowrap}
  .body-copy{color:var(--white);font-size:9.6px;line-height:12.3px}
  .badge{position:absolute;text-align:center;color:var(--white);font-family:"Ubuntu",sans-serif;line-height:1}
  .badge .price{font-weight:700;font-size:27px}
  .badge .what{font-weight:500;font-size:14px;margin-top:3px}
  .badge .fine{font-size:7.5px;margin-top:3px;line-height:1.15}
  .brand-name{position:absolute;color:var(--white);font-family:"Ubuntu",sans-serif;font-weight:500;font-size:19px;line-height:1.15;text-align:center;letter-spacing:1px}
  .services-title{position:absolute;left:0;top:437px;width:173px;height:33px;background:var(--green);border-radius:0 17px 17px 0;color:var(--white);font-family:"Ubuntu",sans-serif;font-weight:500;font-size:19px;line-height:33px;padding-left:28px}
  .services{position:absolute;list-style:none;color:var(--white);font-family:"Ubuntu",sans-serif;font-weight:500;font-size:12px}
  .services li{height:24px;display:flex;align-items:center;gap:6px}
  .services li svg{flex:none}
  .tagline-strip{position:absolute;left:0;top:611px;width:310px;height:20px;background:var(--navy);border-radius:0 10px 10px 0;color:var(--white);font-family:"Ubuntu",sans-serif;font-size:14px;line-height:20px;padding-left:16px;white-space:nowrap}
  .tagline-strip b{font-weight:700}
  .insurance-band{position:absolute;left:0;width:100%;height:30px;background:var(--green);color:var(--white);font-family:"Ubuntu",sans-serif;font-size:19.5px;line-height:30px;text-align:center;white-space:nowrap}
  .footer{position:absolute;left:0;width:100%;bottom:0;background:var(--white);color:var(--ink);text-align:center}
  .footer .address{font-size:12px;margin-top:16px}
  .footer .phone{font-size:15px;letter-spacing:1px;margin-top:3px}
  .hours{position:absolute;left:301px;top:421px;color:var(--white);font-family:"Ubuntu",sans-serif;font-size:15.5px;line-height:20.5px}
  .side-label{position:absolute;top:996px;color:var(--white);font-family:"Ubuntu",sans-serif;font-size:38px;letter-spacing:1px;transform:translateX(-50%)}
</style>
</head>
<body>
<div class="stage">

  <!-- FRONT -->
  <section class="page page--front">
    <svg class="art" width="528" height="739" viewBox="0 0 528 739">
      <defs>
        <linearGradient id="frontTop" x1="0" x2="1"><stop offset="0" stop-color="#f0d9b5"/><stop offset=".55" stop-color="#f4e6dc"/><stop offset="1" stop-color="#e8d2c4"/></linearGradient>
        <linearGradient id="familyFront" x1="0" y1="0" x2="1" y2="1"><stop offset="0" stop-color="#c9b3a2"/><stop offset="1" stop-color="#8e7a6c"/></linearGradient>
      </defs>
      <path d="M0 70 C120 160 330 170 528 118 V158 C330 200 120 190 0 120 Z" fill="var(--green)"/>
      <path role="img" aria-label="Photo of a smiling mother brushing her teeth next to a baby" d="M0 0 H528 V120 C330 160 120 150 0 72 Z" fill="url(#frontTop)"/>
      <circle cx="424" cy="243" r="113" fill="var(--green)"/>
      <circle cx="424" cy="243" r="104" fill="var(--navy)"/>
      <circle cx="432" cy="520" r="115" fill="var(--green)"/>
      <circle cx="432" cy="520" r="110" fill="var(--white)"/>
      <circle role="img" aria-label="Photo of a smiling family of four lying together on a couch" cx="432" cy="520" r="104" fill="url(#familyFront)"/>
      <circle cx="374" cy="347" r="63" fill="var(--white)"/>
      <circle cx="374" cy="347" r="58" fill="var(--green)"/>
      <rect x="36" y="275" width="196" height="2.5" fill="var(--green)"/>
    </svg>

    <div class="brand-name" style="left:336px;top:218px;width:176px">Belcrest Family<br>Dental</div>

    <div class="headline abs" style="left:32px;top:198px;font-size:24px">BE PROUD OF</div>
    <div class="headline abs" style="left:32px;top:226px;font-size:40px">YOUR SMILE</div>

    <p class="body-copy abs" style="left:28px;top:286px;width:280px">The Offer includes exm, cleaning ( prophylaxis) &amp; X - rays .New patients only, Advertised fee is the minimum fee, subject to clinical need. One or more of the following ADA codes may reflect the treatment rendered under this offer, D0150,D0330,D0272,D0210,D1110.*This offers is not to be applied toward account balances or dental services already delivered and not in conjunction with any other offers, discounts or reduced - fee plans. Advertised fee is the minimum fee. Additional fees may be incurred in individual cases. Please contact our office for details.</p>

    <div class="badge" style="left:316px;top:305px;width:116px">
      <div class="price">$ 79</div>
      <div class="what">Cleaning Exam<br>&amp; X - rays</div>
      <div class="fine">(Reg $354)offer<br>expires in 30 days</div>
    </div>

    <div class="services-title">Our Services</div>
    <ul class="services" style="left:22px;top:479px">
      <li><svg width="13" height="13" viewBox="0 0 13 13"><path d="M2 2 C4 0 9 0 11 2 C12 5 10 8 9 12 L7 8 L6 8 L4 12 C3 8 1 5 2 2Z" fill="none" stroke="var(--green)" stroke-width="1.3"/></svg>Dentures</li>
      <li><svg width="13" height="13" viewBox="0 0 13 13"><path d="M2 2 C4 0 9 0 11 2 C12 5 10 8 9 12 L7 8 L6 8 L4 12 C3 8 1 5 2 2Z" fill="none" stroke="var(--green)" stroke-width="1.3"/></svg>Smile designs</li>
      <li><svg width="13" height="13" viewBox="0 0 13 13"><path d="M2 2 C4 0 9 0 11 2 C12 5 10 8 9 12 L7 8 L6 8 L4 12 C3 8 1 5 2 2Z" fill="none" stroke="var(--green)" stroke-width="1.3"/></svg>Bridges</li>
      <li><svg width="13" height="13" viewBox="0 0 13 13"><path d="M2 2 C4 0 9 0 11 2 C12 5 10 8 9 12 L7 8 L6 8 L4 12 C3 8 1 5 2 2Z" fill="none" stroke="var(--green)" stroke-width="1.3"/></svg>Clear Aligner Treatment</li>
      <li><svg width="13" height="13" viewBox="0 0 13 13"><path d="M2 2 C4 0 9 0 11 2 C12 5 10 8 9 12 L7 8 L6 8 L4 12 C3 8 1 5 2 2Z" fill="none" stroke="var(--green)" stroke-width="1.3"/></svg>Take - Home Whitening</li>
    </ul>
    <ul class="services" style="left:190px;top:479px">
      <li><svg width="13" height="13" viewBox="0 0 13 13"><path d="M2 2 C4 0 9 0 11 2 C12 5 10 8 9 12 L7 8 L6 8 L4 12 C3 8 1 5 2 2Z" fill="none" stroke="var(--green)" stroke-width="1.3"/></svg>Extractions</li>
      <li><svg width="13" height="13" viewBox="0 0 13 13"><path d="M2 2 C4 0 9 0 11 2 C12 5 10 8 9 12 L7 8 L6 8 L4 12 C3 8 1 5 2 2Z" fill="none" stroke="var(--green)" stroke-width="1.3"/></svg>Crowns</li>
      <li><svg width="13" height="13" viewBox="0 0 13 13"><path d="M2 2 C4 0 9 0 11 2 C12 5 10 8 9 12 L7 8 L6 8 L4 12 C3 8 1 5 2 2Z" fill="none" stroke="var(--green)" stroke-width="1.3"/></svg>Partials</li>
      <li><svg width="13" height="13" viewBox="0 0 13 13"><path d="M2 2 C4 0 9 0 11 2 C12 5 10 8 9 12 L7 8 L6 8 L4 12 C3 8 1 5 2 2Z" fill="none" stroke="var(--green)" stroke-width="1.3"/></svg>Implant Restoration</li>
      <li><svg width="13" height="13" viewBox="0 0 13 13"><path d="M2 2 C4 0 9 0 11 2 C12 5 10 8 9 12 L7 8 L6 8 L4 12 C3 8 1 5 2 2Z" fill="none" stroke="var(--green)" stroke-width="1.3"/></svg>Oral Cancer Screening</li>
    </ul>

    <div class="tagline-strip">DENTISTRY THAT MAKES <b>DIFFERENCE !</b></div>
    <div class="insurance-band" style="top:639px">Most Insurances Accepted | Payment Options Available</div>
    <div class="footer" style="height:70px">
      <div class="address">4382 W Dunlow rd, Katy, TX 77583</div>
      <div class="phone">9015550142</div>
    </div>
  </section>

  <!-- BACK -->
  <section class="page page--back">
    <svg class="art" width="526" height="737" viewBox="0 0 526 737">
      <defs>
        <linearGradient id="backTop" x1="0" x2="1"><stop offset="0" stop-color="#e4e6e8"/><stop offset=".6" stop-color="#cfc6c2"/><stop offset="1" stop-color="#d9dcdf"/></linearGradient>
        <linearGradient id="coupleBack" x1="0" y1="0" x2="1" y2="1"><stop offset="0" stop-color="#e7cdb5"/><stop offset="1" stop-color="#c9a88f"/></linearGradient>
        <linearGradient id="familyBack" x1="0" y1="0" x2="1" y2="1"><stop offset="0" stop-color="#ead7c6"/><stop offset="1" stop-color="#b9927a"/></linearGradient>
        <linearGradient id="smileBack" x1="0" y1="0" x2="1" y2="1"><stop offset="0" stop-color="#f3e6e0"/><stop offset="1" stop-color="#c43b3b"/></linearGradient>
      </defs>
      <path d="M0 80 C130 170 330 180 526 120 V150 C330 210 130 200 0 130 Z" fill="var(--green)"/>
      <path role="img" aria-label="Photo of gloved hands working on a dental model with a handpiece" d="M0 0 H526 V120 C330 165 130 160 0 80 Z" fill="url(#backTop)"/>
      <circle cx="413" cy="177" r="112" fill="var(--green)"/>
      <circle cx="413" cy="177" r="106" fill="var(--white)"/>
      <circle role="img" aria-label="Photo of a smiling senior couple" cx="413" cy="177" r="100" fill="url(#coupleBack)"/>
      <circle cx="373" cy="321" r="59" fill="var(--white)"/>
      <circle cx="373" cy="321" r="54" fill="var(--green)"/>
      <rect x="33" y="261" width="190" height="2.5" fill="var(--green)"/>
      <circle cx="117" cy="517" r="118" fill="var(--green)"/>
      <circle cx="117" cy="517" r="112" fill="var(--white)"/>
      <circle role="img" aria-label="Photo of a smiling family with two children" cx="117" cy="517" r="106" fill="url(#familyBack)"/>
      <circle cx="253" cy="569" r="56" fill="var(--green)"/>
      <circle cx="253" cy="569" r="52" fill="var(--white)"/>
      <circle role="img" aria-label="Close-up photo of a bright white smile with red lips" cx="253" cy="569" r="47" fill="url(#smileBack)"/>
      <rect x="313" y="487" width="213" height="4" fill="var(--white)"/>
      <rect x="325" y="510" width="201" height="124" fill="var(--green)"/>
      <rect role="img" aria-label="Street map showing the clinic location near Katy, TX" x="327" y="512" width="199" height="120" fill="#eef0ee"/>
      <path d="M430 580 c-5 0 -8 4 -8 8 c0 6 8 14 8 14 s8 -8 8 -14 c0 -4 -3 -8 -8 -8z" fill="#e53935"/>
      <circle cx="430" cy="588" r="2.5" fill="var(--white)"/>
    </svg>

    <div class="headline abs" style="left:33px;top:200px;font-size:25px;line-height:30px">DENTISTRY THAT<br>MAKES DIFFERENCE !</div>

    <p class="body-copy abs" style="left:29px;top:270px;width:276px">Enjoy a $100 savings on all crowns (including bridges and veneers). Subject to clinical need. Call for details. One or more of the following ADA codes may reflect the treatment rendered under this offer. D2740 - D2794, D2962, D6210 - D6245, D6740 - D6792, D6794.* This offer is not to be applied toward account balances or dental services already delivered and not in Conjunction with any other offers, discounts, or reduced - fee plans. Advertised fee is the minimum fee. Additional fees may be incurred in individual cases. Please contact our office for details.</p>

    <div class="badge" style="left:319px;top:278px;width:108px">
      <div class="price" style="font-size:26px">$ 100</div>
      <div class="what" style="font-size:14px;margin-top:1px">Off all Crowns</div>
      <div class="fine" style="font-size:8.5px;font-weight:500">(incuding Bridges &amp;<br>Veneers)</div>
      <div class="fine" style="font-size:6px">(Reg $1,288)offer expires in<br>30 days.<br>New Patients Only</div>
    </div>

    <div class="hours">OPENING TIMES :<br>MON - THUR : 8AM TO 5PM<br>FRIDAY - 8AM TO 3PM</div>

    <div class="insurance-band" style="top:637px">Most Insurances Accepted | Payment Options Available</div>
    <div class="footer" style="height:70px">
      <div class="address" style="margin-top:12px">4382 W Dunlow rd, Katy, TX 77583</div>
      <div class="phone">9015550142</div>
    </div>
  </section>

  <div class="side-label" style="left:302px">FRONT</div>
  <div class="side-label" style="left:854px">BACK</div>
</div>
</body>
</html>
```